Harrowby Wine Label - Design a front and smaller back label for an exclusive red wine

Harrowby Wines produces a very high quality, high priced wine from an old and prestigous vineyard in one of Australia's oldest, but smallest wine growing regions. The grapevines are old (like old men with gnarled arms and trunks) and they produce fewer grapes than younger vines but the grape quality (and thus wine quality) is magnificent and highly sought after as it produces wine of exceptional quality.
The vineyard was purchased by the Harrowby family in February 2010 from a multinational wine company who made wonderful, trophy winning wines for 10 years before the vineyard went into a decline.
The challenge is to produce 2 labels - a simple main front label that focuses on the Harrowby brand and a smaller, information rich, back label that relates the history of the vineyard.
The labels should have a white or charcoal grey background and impart tradition, quality, exclusivity and a little self indulgence which is why we want the family crest incorporated - the choice of font will help.
It might also impart a sense of fun so that it appeals to the 25-35 year old age bracket.
The label should be kept clean and simple not loud and busy. Preferred colours are black, grey and white. Red is fine if used sparingly

Here are the details:_

Front Label (115 long x 65-90mm wide)

Harrowby
Lanternwatch Reserve
2011
Mudgee
Wine of Australia 750ml

Back Label (dimensions to suit text and front label design; font size small; text in black so that it is readable in less than optimal light (eg candlelight at a restaurant table).

Harrowby
Lanternwatch Reserve 2011

This is the first release of The Lanternwatch’s Reserve – just 100 dozen bottles were made. The wine was made from Shiraz and 10% Cabernet Sauvignon grapes sourced from an iconic Mudgee vineyard that was established 1966 by Peter Vallis. In 1994, the vineyard known as ”Silver Hollow”, became the source of a decade of formidable, trophy winning wines under Tindalberg’s and later Quellwood’s ownership. The 20ha vineyard was purchased by Corin & Margaret Harrowby in 2010. The Silver Hollow name was retained by Quellwoods; no wine has been released under this label since the 2006 vintage.

The shaky old Shiraz vines are slowly being restored to full health using careful cane pruning techniques that stimulates fresh, new tissue growth, more even bunch sizes and better grape quality and consistency. The Shiraz grapes used in this wine were hand-picked from two rows of the first crop from the 46 year old, cane pruned vines. The 2011 Reserve is the first step to re-establish the traditions of a famous vineyard and one of Australia’s most sought after export wines.

“Deep and intense purple hues with aromas of ripe blackberry fruits, spice and eucalypt with rich chocolate complemented by subtle oak overtones. A rich and full bodied wine exhibiting a soft yet generous palate with plum, forest fruits and mint chocolate notes. A fine grained tannin structure displaying integrated oak characters adds to the complexity of the wine. This wine was aged for 18 months in a blend of new French oak hogsheads and one year old American hogsheads, crafting a blend with great structure and length of flavour which will develop into a Mudgee classic” – Lewis Farrant, Winemaker

13.5% Alc/Vol.
Contains approx 8.0 std drinks
Preservative (220) added

Harrowby Wines
Tallowbend Rd, Mudgee 2850
www.harrowbywines.example.au

Reason: My apologies to the designers who have kindly submitted some wonderful designs. I am trying to achieve a conscentious between shareholders. This is difficult as they are in different parts of the world and I have learned through this experience that opinions on wine labels are quite diverse!!! The feedback I have received so far indicates the following (1) A light or white background is preferred (2) The crest should not be a dominant part of the label (3) The label needs to be clean, fresh and uncomplicated (4) If red is used it should be in minor detail only (5) "Harrowby" should be distinctive. The font is difficult for us! (6) We are considering "The Lanternwatch" RESERVE instead of "Lanternwatch's" RESERVE (7) The text on the back label is too long; I will edit and re-upload Many thanks for your help and patience Kind regards Corin

Good Morning All,
I have edited the back label text to reduce the size of the label. A Word file with the changes has just been uploaded.
Cheers
Corin

Dear Designers,
Thank you all so very much for the wonderful selection of designs you have submitted my family have all been overwhelmed by the quality and skill level exhibited and we all appreciate you your efforts
Kindest regards
Corin

Target Market(s)

25-35 year old men and women of Australia, China, US & UK

Industry/Entity Type

Restaurant

Requirements
Must have
• Crest
Should not have
• Animals on the label

```html
<!DOCTYPE html>
<html lang="en">
<head>
<meta charset="utf-8">
<title>Harrowby Wine Label – Lanternwatch Reserve 2011</title>
<link rel="stylesheet" href="https://fonts.googleapis.com/css2?family=Pinyon+Script&family=Tangerine:wght@400;700&family=IM+Fell+English:ital@0;1&display=swap">
<style>
  :root {
    --page: #f4f4f4;
    --label-light: #c9c9c9;
    --label-mid: #a9a9a9;
    --label-dark: #6f6f6f;
    --label-edge: #4a4a4a;
    --ink: #1c1c1c;
    --ink-soft: #2e2e2e;
    --crest-light: #bdbdbd;
    --crest-dark: #7a7a7a;
  }
  * { box-sizing: border-box; margin: 0; padding: 0; }
  html, body {
    width: 825px;
    height: 1200px;
    overflow: hidden;
    background: var(--page);
  }
  .canvas {
    position: relative;
    width: 825px;
    height: 1200px;
  }
  .label {
    position: absolute;
    background:
      radial-gradient(ellipse at 50% 45%, var(--label-light) 0%, var(--label-mid) 55%, var(--label-dark) 90%, var(--label-edge) 100%);
    box-shadow: inset 0 0 30px rgba(0,0,0,0.45);
    color: var(--ink);
  }

  /* Front label */
  .front-label {
    left: 40px;
    top: 290px;
    width: 400px;
    height: 610px;
    text-align: center;
  }
  .brand-name {
    position: absolute;
    top: 26px;
    left: 0;
    right: 0;
    font-family: "Pinyon Script", cursive;
    font-size: 64px;
    line-height: 1;
    color: var(--ink-soft);
  }
  .crest {
    position: absolute;
    top: 112px;
    left: 100px;
    width: 200px;
    height: 270px;
  }
  .vintage-name {
    position: absolute;
    top: 420px;
    left: 0;
    right: 0;
    font-family: "Tangerine", cursive;
    font-weight: 700;
    font-size: 40px;
    line-height: 1;
  }
  .region {
    position: absolute;
    top: 475px;
    left: 0;
    right: 0;
    font-family: "Tangerine", cursive;
    font-weight: 700;
    font-size: 58px;
    line-height: 1;
  }
  .volume {
    position: absolute;
    right: 18px;
    bottom: 14px;
    font-family: "IM Fell English", serif;
    font-style: italic;
    font-size: 11px;
    color: var(--ink-soft);
  }

  /* Back label */
  .back-label {
    left: 470px;
    top: 290px;
    width: 320px;
    height: 610px;
    padding: 18px 20px;
    font-family: "IM Fell English", serif;
    font-style: italic;
    font-size: 9.6px;
    line-height: 1.24;
  }
  .back-title {
    font-family: "Pinyon Script", cursive;
    font-style: normal;
    font-size: 26px;
    line-height: 1;
    text-align: center;
  }
  .back-subtitle {
    font-family: "Tangerine", cursive;
    font-style: normal;
    font-weight: 700;
    font-size: 20px;
    text-align: center;
    margin-bottom: 8px;
  }
  .story p { margin-bottom: 7px; text-align: justify; }
  .facts, .winery {
    margin-top: 6px;
    line-height: 1.3;
  }
</style>
</head>
<body>
<main class="canvas">

  <section class="label front-label">
    <h1 class="brand-name">Harrowby</h1>
    <svg class="crest" viewBox="0 0 200 270" role="img" aria-label="Harrowby family crest with scroll, wreath and shield bearing gates">
      <defs>
        <linearGradient id="crestTone" x1="0" y1="0" x2="0" y2="1">
          <stop offset="0" stop-color="var(--crest-light)"/>
          <stop offset="1" stop-color="var(--crest-dark)"/>
        </linearGradient>
      </defs>
      <rect x="0" y="0" width="200" height="270" rx="10" fill="url(#crestTone)" opacity="0.6"/>
    </svg>
    <p class="vintage-name">2011 Lanternwatch’s Reserve</p>
    <p class="region">Mudgee</p>
    <p class="volume">Wine of Australia 750ml</p>
  </section>

  <section class="label back-label">
    <h2 class="back-title">Harrowby</h2>
    <p class="back-subtitle">Lanternwatch Reserve 2011</p>
    <div class="story">
      <p>This is the first release of The Lanternwatch’s Reserve – just 100 dozen bottles were made. The wine was made from Shiraz and 10% Cabernet Sauvignon grapes sourced from an iconic Mudgee vineyard that was established 1966 by Peter Vallis. In 1994, the vineyard known as ”Silver Hollow”, became the source of a decade of formidable, trophy winning wines under Tindalberg’s and later Quellwood’s ownership. The 20ha vineyard was purchased by Corin &amp; Margaret Harrowby in 2010.</p>
      <p>The shaky old Shiraz vines are slowly being restored to full health using careful cane pruning techniques that stimulate fresh, new growth and better grape quality. The 2011 Reserve is the first step to re-establish the traditions of a famous vineyard and one of Australia’s most sought after export wines.</p>
      <p>“Deep and intense purple hues with aromas of ripe blackberry fruits, spice and eucalypt with rich chocolate complemented by subtle oak overtones. A rich and full bodied wine exhibiting a soft yet generous palate with plum, forest fruits and mint chocolate notes. Aged for 18 months in new French and one year old American hogsheads, crafting a blend with great structure and length of flavour which will develop into a Mudgee classic” – Lewis Farrant, Winemaker</p>
    </div>
    <p class="facts">13.5% Alc/Vol.<br>Contains approx 8.0 std drinks<br>Preservative (220) added</p>
    <p class="winery">Harrowby Wines<br>Tallowbend Rd, Mudgee 2850<br>www.harrowbywines.example.au</p>
  </section>

</main>
</body>
</html>
```